Consulting company needs Business Cards - rough concept provided

I'm looking for someone to take our business card idea and make is slick and polished - to communicate our high-end, sophisticated, serious consulting business. We have a rough layout we did in-house. We are open to ideas on repo-ing elements, adjusting sizes, typefaces etc... within the general concept we've already come up with. We want it to be super-clean and sophisticated. We want to keep the white backgrounds, and blue brand colors. Our goal is to print with painted blue edges on thick cardstock. Thank you!!

```html
<!DOCTYPE html>
<html lang="en">
<head>
<meta charset="utf-8">
<title>Brinmoral Business Cards</title>
<link href="https://fonts.googleapis.com/css2?family=Jost:wght@400;700&display=swap" rel="stylesheet">
<style>
  :root {
    --brand-blue: #009ddc;
    --ink-grey: #555a5e;
    --soft-grey: #cfd1d3;
    --paper: #ffffff;
    --backdrop: #2f3133;
  }
  html, body {
    margin: 0;
    width: 1200px;
    height: 866px;
    overflow: hidden;
    background: var(--backdrop);
    font-family: "Jost", "Futura", sans-serif;
  }
  .sheet {
    display: flex;
    gap: 40px;
    justify-content: center;
    align-items: center;
    width: 1200px;
    height: 866px;
  }
  .card {
    position: relative;
    width: 520px;
    height: 297px;
    overflow: hidden;
    box-shadow: 0 12px 30px rgba(0,0,0,0.45);
  }
  .card--front { background: var(--paper); }
  .card--back {
    background: var(--brand-blue);
    display: flex;
    align-items: center;
    justify-content: center;
  }
  .contact {
    position: absolute;
    left: 30px;
    top: 34px;
  }
  .contact__name {
    margin: 0;
    color: var(--brand-blue);
    font-weight: 700;
    font-size: 17px;
    line-height: 22px;
    letter-spacing: 0.5px;
    text-transform: uppercase;
  }
  .contact__role {
    margin: 0 0 10px;
    color: var(--ink-grey);
    font-size: 12px;
    letter-spacing: 0.8px;
  }
  .contact__line {
    display: flex;
    align-items: center;
    gap: 7px;
    margin: 0 0 3px;
    color: var(--ink-grey);
    font-size: 12px;
    letter-spacing: 0.4px;
  }
  .contact__line svg { width: 11px; height: 11px; fill: var(--brand-blue); }
  .rule {
    position: absolute;
    left: 206px;
    right: 30px;
    top: 60px;
    height: 1px;
    background: var(--brand-blue);
  }
  .wordmark {
    margin: 0;
    font-weight: 700;
    text-transform: uppercase;
    letter-spacing: 1px;
    line-height: 1;
  }
  .card--front .wordmark {
    position: absolute;
    right: 30px;
    top: 112px;
    font-size: 36px;
    color: var(--brand-blue);
  }
  .card--back .wordmark {
    font-size: 50px;
    color: var(--paper);
  }
  .address {
    position: absolute;
    right: 30px;
    bottom: 54px;
    margin: 0;
    text-align: right;
    color: var(--ink-grey);
    font-size: 12px;
    letter-spacing: 0.8px;
    line-height: 1.4;
  }
  .edge-band {
    position: absolute;
    left: 0;
    bottom: 0;
    width: 520px;
    height: 44px;
  }
</style>
</head>
<body>
<main class="sheet">
  <section class="card card--front" aria-label="Card front">
    <div class="contact">
      <h1 class="contact__name">Dana Whitford</h1>
      <p class="contact__role">Brand Consultant</p>
      <p class="contact__line">
        <svg viewBox="0 0 24 24" aria-hidden="true"><path d="M6.6 10.8a15.2 15.2 0 0 0 6.6 6.6l2.2-2.2a1 1 0 0 1 1-.25 11.4 11.4 0 0 0 3.6.57 1 1 0 0 1 1 1V20a1 1 0 0 1-1 1A17 17 0 0 1 3 4a1 1 0 0 1 1-1h3.5a1 1 0 0 1 1 1c0 1.25.2 2.45.57 3.6a1 1 0 0 1-.25 1z"/></svg>
        (555) 014 2290
      </p>
      <p class="contact__line">
        <svg viewBox="0 0 24 24" aria-hidden="true"><path d="M2 5h20v14H2z M2 5l10 8 10-8" fill="none" stroke="#009ddc" stroke-width="2.4"/></svg>
        dana@brinmoral.com
      </p>
    </div>
    <div class="rule"></div>
    <p class="wordmark">Brinmoral</p>
    <p class="address">4820 Harbor Ave<br>Ste 210 Lakeview, CA 90000</p>
    <svg class="edge-band" viewBox="0 0 520 44" preserveAspectRatio="none" aria-hidden="true">
      <path d="M0 30 L200 40 L200 44 L0 44 Z" fill="var(--soft-grey)"/>
      <path d="M0 37 L170 44 L0 44 Z" fill="var(--brand-blue)"/>
      <path d="M170 44 C190 30 205 22 225 24 C245 26 250 30 270 30 L520 30 L520 44 Z" fill="var(--brand-blue)"/>
    </svg>
  </section>

  <section class="card card--back" aria-label="Card back">
    <p class="wordmark">Brinmoral</p>
  </section>
</main>
</body>
</html>
```